Business card design needed

Want the logo on a medium blue background and a nice funky design. I have my own gym and run one on one personal training and nutrition sessions. want it to look lively.
Updates

Please note I requested my logo on a blue background 

PLEASE NOTE: I already have a logo. It is attached to the order!!

Target Market(s)

over 55s

Industry/Entity Type

Nutrition

Contact Information for Business Card

Front of card : Logo ( on blue background )
Corinne Dalby
Nutrition & Fitness Coach for Seniors
Private gym at : 17 Fennick Street, Brantwood, Perth, WA 6291
Mob : 0412736158
Email : corinnedalby@fernpost.example
"For Seniors by a Senior"

Back of card
B.A. ( Soc.)
Dip. Ed. (Sec.)
Wellness Coach
Cert 4 Personal Trainer
Cert. Nutritition
MOVE ON Facilitator
Ageing Well Moving Freely Facilitator
NLP Master

```html
<!DOCTYPE html>
<html lang="en">
<head>
<meta charset="utf-8">
<title>Corinne Dalby – Business Card</title>
<link href="https://fonts.googleapis.com/css2?family=Open+Sans:ital,wght@0,400;0,600;0,700;1,400;1,600&display=swap" rel="stylesheet">
<style>
  :root {
    --canvas: #e9e6e2;
    --brand-blue: #0d5a8f;
    --deep-blue: #0a4470;
    --back-blue-top: #1c6a9e;
    --back-blue-bottom: #0e4a76;
    --sky-blue: #1aa6e0;
    --sun-yellow: #f5dc1e;
    --sun-soft: #faf0a8;
    --ink: #333a40;
    --white: #ffffff;
  }
  * { margin: 0; padding: 0; box-sizing: border-box; }
  html, body {
    width: 1200px; height: 867px; overflow: hidden;
    background: var(--canvas);
    font-family: "Open Sans", Arial, sans-serif;
  }
  .canvas { position: relative; width: 1200px; height: 867px; }

  .card {
    position: absolute;
    border-radius: 16px;
    overflow: hidden;
    box-shadow: 0 8px 24px rgba(0,0,0,0.18);
  }

  /* Back of card */
  .card-back {
    left: 60px; top: 70px; width: 600px; height: 343px;
    background: linear-gradient(180deg, var(--back-blue-top), var(--back-blue-bottom));
    color: var(--white);
  }
  .card-back .brand-mark {
    position: absolute; top: 46px; left: 0; right: 0;
    display: flex; justify-content: center; align-items: center; gap: 10px;
    font-size: 18px; font-weight: 600; color: #cfe4f3;
  }
  .brand-dot {
    width: 14px; height: 14px; border-radius: 50%;
    background: var(--sun-yellow); flex: none;
  }
  .credentials {
    position: absolute; top: 126px; left: 60px; right: 60px;
    text-align: center; font-style: italic; font-size: 14px; line-height: 1.4;
  }
  .credentials .rule {
    height: 1px; background: rgba(255,255,255,0.75); margin: 10px 0 12px;
  }

  /* Front of card */
  .card-front {
    left: 440px; top: 440px; width: 700px; height: 390px;
    background: var(--white);
  }
  .feature-art {
    position: absolute; left: 0; top: 0; width: 420px; height: 344px;
    background: radial-gradient(circle 145px at 228px 165px,
      var(--sun-soft) 0 74px,
      rgba(13,90,143,0.16) 76px,
      rgba(13,90,143,0.08) 115px,
      rgba(13,90,143,0) 145px);
  }
  .tagline {
    position: absolute; left: 148px; top: 143px; width: 160px;
    text-align: center; font-style: italic; font-weight: 600;
    font-size: 17px; line-height: 1.3; color: var(--deep-blue);
  }
  .card-front .brand-mark {
    position: absolute; top: 34px; right: 60px; width: 220px;
    display: flex; align-items: center; gap: 10px;
    font-size: 17px; font-weight: 600; line-height: 1.2; color: var(--brand-blue);
  }
  .person {
    position: absolute; right: 36px; top: 150px; text-align: right;
  }
  .person-name {
    font-size: 34px; font-weight: 700; color: var(--brand-blue); line-height: 1.1;
  }
  .person-role {
    font-size: 17px; color: var(--sky-blue); margin-top: 6px;
  }
  .gym-address {
    position: absolute; right: 36px; top: 258px; text-align: right;
    font-size: 16px; font-weight: 600; color: var(--ink); line-height: 1.35;
  }
  .contact-band {
    position: absolute; left: 0; right: 0; bottom: 0; height: 46px;
    background: var(--brand-blue); color: var(--white);
    display: flex; align-items: center; justify-content: flex-end; gap: 22px;
    padding-right: 120px;
    font-size: 17px; font-weight: 700;
  }
</style>
</head>
<body>
<main class="canvas">

  <section class="card card-back" aria-label="Back of business card">
    <div class="brand-mark"><span class="brand-dot"></span>Silver Stride Nutrition &amp; Fitness</div>
    <div class="credentials">
      <p>B.A. ( Soc.), Dip. Ed. (Sec.), Cert 4 Personal Trainer, Wellness Coach,</p>
      <div class="rule"></div>
      <p>MOVE ON Facilitator, Ageing Well Moving Freely facilitator, NLP Master.</p>
    </div>
  </section>

  <section class="card card-front" aria-label="Front of business card">
    <div class="feature-art" role="img" aria-label="Decorative brand artwork in blue and yellow"></div>
    <p class="tagline">For Seniors<br>by a Senior</p>

    <div class="brand-mark"><span class="brand-dot"></span><span>Silver Stride<br>Nutrition &amp; Fitness</span></div>

    <div class="person">
      <h1 class="person-name">Corinne Dalby</h1>
      <p class="person-role">Nutrition &amp; Fitness Coach for Seniors</p>
    </div>

    <p class="gym-address">Private gym at:<br>17 Fennick Street, Brantwood, Perth, WA 6291</p>

    <div class="contact-band">
      <span class="phone">0412736158</span>
      <span class="divider">|</span>
      <span class="email">corinnedalby@fernpost.example</span>
    </div>
  </section>

</main>
</body>
</html>
```